menu for prepared meals company

Currently have a menu set up with company logo, would like something more eye catching and artistic to make it look professional. This is a fitness and health driven company in regards to purchasing prepared meals to use towards fitness goals. Do not necessarily want the menu to be geared towards muscular men and women. Looking to have the menu be simple to understand, exactly what it stands for, and geared towards a large demographic in health and life style eating changes.

Target Market(s)

health/fitness

Industry/Entity Type

It Company

Requirements
Must have
• *please see set up for mock menu and apply changes that were applied in the word document menu information.
• ex:do not offer sweet potato and chicken hash*

```html
<!DOCTYPE html>
<html lang="en">
<head>
<meta charset="utf-8">
<title>Fit Plate Kitchen – The Menu</title>
<link rel="stylesheet" href="https://fonts.googleapis.com/css2?family=Oswald:wght@500;600&family=Crimson+Pro:wght@400;600;700&family=Sacramento&family=Josefin+Sans:wght@400&display=swap">
<style>
  :root{
    --page:#ffffff;
    --panel-top:#f3c457;
    --panel-bottom:#d8a22c;
    --panel-shade:#e3ad3c;
    --paper-top:#f4dfb2;
    --paper-bottom:#f9eedb;
    --band:#f3c23e;
    --item-head-a:#ee9c55;
    --item-head-b:#f6c47d;
    --item-body:#f6d596;
    --table-head:#f1a65c;
    --table-body:#f5d392;
    --ink:#2d1f14;
    --heading-ink:#2a1c10;
    --cloche:#e0792c;
    --brand:#c6293a;
    --white:#ffffff;
  }
  *{box-sizing:border-box;margin:0;padding:0}
  html,body{width:1200px;height:900px;overflow:hidden;background:var(--page)}
  body{position:relative;font-family:"Crimson Pro",Georgia,serif;color:var(--ink)}
  .menu{position:absolute;left:13px;top:12px;width:1175px;height:826px;background:linear-gradient(180deg,var(--paper-top),var(--paper-bottom));overflow:hidden}
  .side{position:absolute;left:0;top:0;width:265px;height:826px;background:linear-gradient(180deg,var(--panel-top),var(--panel-bottom));overflow:hidden}
  .side-art{position:absolute;left:70px;top:0;width:130px;height:826px;background:linear-gradient(180deg,rgba(214,160,50,.25),rgba(190,130,30,.25));}
  .brand-ring{position:absolute;left:51px;top:265px;width:164px;height:164px;border-radius:50%;background:var(--panel-shade);}
  .brand-badge{position:absolute;left:60px;top:274px;width:146px;height:146px;border-radius:50%;background:var(--white);display:flex;align-items:center;justify-content:center;text-align:center;}
  .brand-name{font-family:"Crimson Pro",Georgia,serif;font-weight:700;font-size:26px;line-height:1.05;color:var(--brand);}
  .menu-title{position:absolute;left:56px;top:600px;width:190px;height:100px;color:var(--white);}
  .menu-title .the{position:absolute;left:94px;top:18px;font-family:"Josefin Sans",sans-serif;font-size:20px;letter-spacing:4px;line-height:1;}
  .menu-title .word{position:absolute;left:0;top:22px;font-family:"Sacramento",cursive;font-size:72px;line-height:1;white-space:nowrap;}
  .cloche{position:absolute;width:30px;height:22px}
  .band{position:absolute;height:40px;background:var(--band);display:flex;align-items:center;padding-left:26px;font-family:"Oswald",sans-serif;font-weight:500;font-size:19px;color:var(--heading-ink);white-space:nowrap;}
  .band .price{margin-left:24px}
  .item-head{position:absolute;left:305px;width:242px;height:40px;background:linear-gradient(90deg,var(--item-head-a),var(--item-head-b));font-weight:700;font-size:13px;padding:10px 0 0 24px;}
  .item-body{position:absolute;left:305px;width:242px;background:var(--item-body);font-size:13px;line-height:14px;padding:7px 0 0 24px;opacity:.85}
  .table{position:absolute;background:var(--table-body);}
  .table-head{height:42px;background:linear-gradient(90deg,var(--table-head),#f5c07a);display:flex;align-items:center;font-weight:700;font-size:13px;line-height:14px;}
  .row{display:flex;align-items:center;height:27.5px;font-size:13px;white-space:nowrap}
  .c1{padding-left:22px}
  .cc{text-align:center}
  .notes{position:absolute;left:855px;top:530px;width:245px;font-size:12.5px;line-height:14px;}
  .notes p{padding-left:10px;text-indent:-10px;margin-bottom:13px}
</style>
</head>
<body>
<div class="menu">
  <aside class="side">
    <div class="side-art" role="img" aria-label="Faint tall utensil decoration"></div>
    <div class="brand-ring"></div>
    <div class="brand-badge"><span class="brand-name">Fit Plate<br>Kitchen</span></div>
    <div class="menu-title"><span class="the">THE</span><span class="word">Menu</span></div>
  </aside>

  <svg class="cloche" style="left:488px;top:17px" viewBox="0 0 30 22"><circle cx="15" cy="4" r="2.5" fill="var(--cloche)"/><path d="M3 18 A12 12 0 0 1 27 18 Z" fill="var(--cloche)"/><rect x="1" y="18" width="28" height="3" fill="var(--cloche)"/></svg>
  <svg class="cloche" style="left:766px;top:17px" viewBox="0 0 30 22"><circle cx="15" cy="4" r="2.5" fill="var(--cloche)"/><path d="M3 18 A12 12 0 0 1 27 18 Z" fill="var(--cloche)"/><rect x="1" y="18" width="28" height="3" fill="var(--cloche)"/></svg>
  <svg class="cloche" style="left:1041px;top:17px" viewBox="0 0 30 22"><circle cx="15" cy="4" r="2.5" fill="var(--cloche)"/><path d="M3 18 A12 12 0 0 1 27 18 Z" fill="var(--cloche)"/><rect x="1" y="18" width="28" height="3" fill="var(--cloche)"/></svg>

  <div class="band" style="left:305px;top:42px;width:248px">Specialty Meals<span class="price">$9.95</span></div>
  <div class="band" style="left:582px;top:42px;width:246px">Create Your Own &nbsp;- &nbsp;Part 1</div>
  <div class="band" style="left:857px;top:42px;width:246px">Create Your Own &nbsp;- &nbsp;Part 2</div>

  <div class="item-head" style="top:93px">Pasta with Turkey Meatballs</div>
  <div class="item-body" style="top:133px;height:42px">Whole Grain Pasta<br>with Turkey Meatballs &amp; Tomato Sauce</div>
  <div class="item-head" style="top:206px">Stir Fry</div>
  <div class="item-body" style="top:246px;height:44px">Chicken, Stir Fry Vegetable Mix<br>with Jasmine Rice</div>
  <div class="item-head" style="top:320px">Turkey Burger</div>
  <div class="item-body" style="top:360px;height:44px">Turkey Patty on a Multigram Flat Bread<br>with side of sweet potato fries</div>
  <div class="item-head" style="top:436px">Stuffed Pepper</div>
  <div class="item-body" style="top:476px;height:60px">Pepper stuffed with Ground Turkey<br>Your Choice of Whole Grain or<br>Jasmine Rice Combined in a Red Sauce</div>

  <div class="table" style="left:582px;top:93px;width:240px;height:198px">
    <div class="table-head"><span class="c1" style="width:124px">Choose Protein</span><span class="cc" style="width:52px">Half Size<br>(4 Oz)</span><span class="cc" style="width:60px">Full Size<br>(8 Oz)</span></div>
    <div style="padding-top:4px">
      <div class="row"><span class="c1" style="width:124px">Chicken</span><span class="cc" style="width:52px">$7.95</span><span class="cc" style="width:60px">$8.95</span></div>
      <div class="row"><span class="c1" style="width:124px">Ground Beef</span><span class="cc" style="width:52px">$7.95</span><span class="cc" style="width:60px">$8.95</span></div>
      <div class="row"><span class="c1" style="width:124px">Ground Turkey</span><span class="cc" style="width:52px">$7.95</span><span class="cc" style="width:60px">$8.95</span></div>
      <div class="row"><span class="c1" style="width:124px">Steak</span><span class="cc" style="width:52px">$9.95</span><span class="cc" style="width:60px">$10.95</span></div>
      <div class="row"><span class="c1" style="width:124px">Turkey Tenderloin</span><span class="cc" style="width:52px">$7.95</span><span class="cc" style="width:60px">$8.95</span></div>
    </div>
  </div>

  <div class="table" style="left:582px;top:296px;width:240px;height:157px;background:rgba(245,211,146,.55)">
    <div class="row" style="height:28px;font-weight:700;padding-top:4px"><span class="c1">All Fish Portions are 6 Oz</span></div>
    <div class="row"><span class="c1" style="width:140px">Salmon</span><span class="cc" style="width:70px">$11.95</span></div>
    <div class="row"><span class="c1" style="width:140px">Tilapia</span><span class="cc" style="width:70px">$10.95</span></div>
    <div class="row"><span class="c1" style="width:140px">Cod</span><span class="cc" style="width:70px">$9.95</span></div>
    <div class="row"><span class="c1" style="width:140px">Veggie Burger</span><span class="cc" style="width:70px">$9.95</span></div>
  </div>

  <div class="table" style="left:857px;top:93px;width:240px;height:200px">
    <div class="table-head"><span class="c1" style="width:119px">Carb Choices</span><span class="cc" style="width:56px">Half Size<br>(1/2 Cup)</span><span class="cc" style="width:62px">Full Size<br>(1 Cup)</span></div>
    <div style="padding-top:4px">
      <div class="row"><span class="c1" style="width:119px">Whole Grain Pasta</span><span class="cc" style="width:56px">$</span><span class="cc" style="width:62px">$</span></div>
      <div class="row"><span class="c1" style="width:119px">Whole Grain Rice</span><span class="cc" style="width:56px">$</span><span class="cc" style="width:62px">$</span></div>
      <div class="row"><span class="c1" style="width:119px">Jasmine Rice</span><span class="cc" style="width:56px">$</span><span class="cc" style="width:62px">$</span></div>
      <div class="row"><span class="c1" style="width:119px">Sweet Potato</span><span class="cc" style="width:56px">$</span><span class="cc" style="width:62px">$</span></div>
    </div>
  </div>

  <div class="table" style="left:857px;top:311px;width:240px;height:197px">
    <div class="table-head"><span class="c1" style="width:119px">Vege Choices</span><span class="cc" style="width:56px">Half Size<br>(1/2 Cup)</span><span class="cc" style="width:62px">Full Size<br>(1 Cup)</span></div>
    <div style="padding-top:4px">
      <div class="row"><span class="c1" style="width:119px">Green Beans</span><span class="cc" style="width:56px">$</span><span class="cc" style="width:62px">$</span></div>
      <div class="row"><span class="c1" style="width:119px">Broccoli</span><span class="cc" style="width:56px">$</span><span class="cc" style="width:62px">$</span></div>
      <div class="row"><span class="c1" style="width:119px">Spinach</span><span class="cc" style="width:56px">$</span><span class="cc" style="width:62px">$</span></div>
      <div class="row"><span class="c1" style="width:119px">Asparagus</span><span class="cc" style="width:56px">$</span><span class="cc" style="width:62px">$</span></div>
    </div>
  </div>

  <div class="notes">
    <p>* If two vegetable options are wanted they may choose two for low carb meal combo.</p>
    <p>* Also offer gluten free pasta as a carb option.</p>
    <p>* Offer at home or delivery within 20 miles for small fee.</p>
  </div>
</div>
</body>
</html>
```